Simple, Professional and neat business card design for Vendralo Inc.

We're looking to re-vamp our business card design. We're a supplier of innovative feed ingredients for the North American animal agriculture industry. We are located in Lucknow, Ontario, Canada and our flagship product is a product that prevents milk fever in dairy cows when the calve, it is fed before calving and is very effective compared to other alternatives available on the market today.

Our company has Danish roots and we import all of our product from our Danish partner/manufacturer in Denmark. We like our design to embrace high professionalism while remaining neat and simple.

Target Market(s)

B2B, Feed Mills, Veterinary Clinics, Large integrators/producers,

Industry/Entity Type

Agribusiness

Contact Information for Business Card

We like the rounded corners because they make the card easy to sit in a wallet and not many use it so it makes the card stand out, just possibly something to take account for during the design.

As you can also see on the sliders below, looking for a that simple but proffesional scandinavian design.

Requirements
Nice to have
• Rounded corners
Should not have
• Too vibrant

```html
<!DOCTYPE html>
<html lang="en">
<head>
<meta charset="utf-8">
<title>Vendralo Inc. Business Card</title>
<link rel="stylesheet" href="https://fonts.googleapis.com/css2?family=Lato:wght@400;700;900&display=swap">
<style>
  :root {
    --bg: #2a2724;
    --card-white: #ffffff;
    --brand-blue: #0b57a4;
    --brand-gold: #d9bd86;
    --ink: #1f1f1f;
    --ink-soft: #333333;
  }
  * { box-sizing: border-box; margin: 0; padding: 0; }
  html, body { width: 1200px; height: 1200px; overflow: hidden; }
  body {
    background: var(--bg);
    font-family: "Lato", sans-serif;
    position: relative;
  }
  .card {
    position: absolute;
    left: 266px;
    width: 668px;
    height: 382px;
    border-radius: 26px;
    overflow: hidden;
    box-shadow: 0 6px 18px rgba(0,0,0,0.45);
  }
  .card--front { top: 196px; background: var(--card-white); }
  .card--back {
    top: 629px;
    background: var(--brand-blue);
    display: flex;
    align-items: center;
    justify-content: center;
  }

  /* front brand block */
  .brand-front {
    position: absolute;
    left: 40px;
    top: 70px;
    width: 290px;
    text-align: center;
  }
  .brand-mark {
    display: block;
    width: 64px;
    height: 64px;
    border-radius: 50%;
    background: var(--brand-blue);
    margin: 0 auto 42px;
  }
  .brand-name {
    color: var(--brand-blue);
    font-weight: 900;
    font-size: 24px;
    letter-spacing: 0.2px;
    text-transform: uppercase;
    line-height: 1;
  }
  .brand-tagline {
    color: var(--ink-soft);
    font-size: 16px;
    margin-top: 6px;
  }

  .social-label {
    position: absolute;
    right: 38px;
    top: 72px;
    color: var(--brand-blue);
    font-size: 13px;
    font-weight: 700;
    letter-spacing: 0.5px;
  }

  /* name tab */
  .name-tab {
    position: absolute;
    left: 370px;
    right: -30px;
    top: 102px;
    height: 132px;
    background: var(--brand-blue);
    border: 4px solid var(--brand-gold);
    border-radius: 30px 0 0 30px;
    padding: 12px 0 0 18px;
    color: #ffffff;
  }
  .person-name {
    color: var(--brand-gold);
    font-weight: 700;
    font-size: 28px;
    letter-spacing: 1.5px;
    text-transform: uppercase;
    line-height: 1.1;
  }
  .person-phone { font-weight: 700; font-size: 18px; margin-top: 6px; }
  .person-address { font-size: 16px; line-height: 1.2; margin-top: 6px; }

  /* contact row */
  .contact-row {
    position: absolute;
    top: 304px;
    left: 0;
    right: 0;
  }
  .contact-item {
    position: absolute;
    display: flex;
    align-items: center;
    gap: 10px;
    color: var(--ink);
    font-size: 16px;
    line-height: 1.3;
  }
  .contact-item--phone { left: 34px; }
  .contact-item--fax { left: 276px; }
  .contact-item--web { left: 445px; }
  .contact-icon {
    flex: none;
    width: 34px;
    height: 34px;
    border-radius: 7px;
    background: var(--brand-blue);
    display: flex;
    align-items: center;
    justify-content: center;
  }
  .accent { color: var(--brand-blue); }

  /* back */
  .brand-back {
    display: flex;
    align-items: center;
    gap: 26px;
    margin-bottom: 16px;
  }
  .brand-back .brand-mark {
    width: 88px;
    height: 88px;
    margin: 0;
    background: var(--brand-gold);
  }
  .brand-back-name {
    color: #ffffff;
    font-weight: 900;
    font-size: 53px;
    line-height: 1;
    text-transform: uppercase;
  }
  .brand-back-tagline {
    color: #ffffff;
    font-size: 17px;
    letter-spacing: 3px;
    margin-top: 8px;
  }
</style>
</head>
<body>
  <section class="card card--front">
    <div class="brand-front">
      <span class="brand-mark"></span>
      <div class="brand-name">Vendralo Inc.</div>
      <div class="brand-tagline">Protecting the health of your animals</div>
    </div>

    <div class="social-label">Social</div>

    <div class="name-tab">
      <div class="person-name">Henrik Mollsen</div>
      <div class="person-phone">555-214-0190</div>
      <div class="person-address">Box 48, Elmridge<br>Ontario Canada N0X 1A0</div>
    </div>

    <div class="contact-row">
      <div class="contact-item contact-item--phone">
        <span class="contact-icon">
          <svg width="20" height="20" viewBox="0 0 24 24" fill="#fff"><path d="M3 9c0-3 4-5 9-5s9 2 9 5v2h-5V9c-1-1-7-1-8 0v2H3z"/><rect x="5" y="12" width="14" height="8" rx="2"/></svg>
        </span>
        <span>555-214-7736<br>555-214-0190 <span class="accent">(Toll Free)</span></span>
      </div>
      <div class="contact-item contact-item--fax">
        <span class="contact-icon">
          <svg width="20" height="20" viewBox="0 0 24 24" fill="#fff"><rect x="7" y="3" width="10" height="5"/><rect x="3" y="8" width="18" height="9" rx="2"/><rect x="7" y="14" width="10" height="7" fill="#fff" stroke="#0b57a4" stroke-width="1.5"/></svg>
        </span>
        <span>555-214-7736</span>
      </div>
      <div class="contact-item contact-item--web">
        <span class="contact-icon">
          <svg width="20" height="20" viewBox="0 0 24 24" fill="none" stroke="#fff" stroke-width="2"><circle cx="12" cy="12" r="9"/><ellipse cx="12" cy="12" rx="4" ry="9"/><line x1="3" y1="12" x2="21" y2="12"/></svg>
        </span>
        <span>henrik@<span class="accent">vendralo</span>.com<br>www.<span class="accent">vendralo</span>.com</span>
      </div>
    </div>
  </section>

  <section class="card card--back">
    <div>
      <div class="brand-back">
        <span class="brand-mark"></span>
        <div>
          <div class="brand-back-name">Vendralo Inc.</div>
          <div class="brand-back-tagline">Protecting the health of your animals</div>
        </div>
      </div>
    </div>
  </section>
</body>
</html>
```